Tales from Kin Logo Design plus business cards design

We are a start up company that will help seniors write their memoirs...beginning with a few ancestors and their heritage and continuing through their own history...how they would like to be remembered in the next generation. I envision a card with a senior citizen at an older writing desk, writing her memoirs, with a book (maybe standing on top, leaning slightly) that has the words Tales from Kin.com on the back binding. OR maybe a senior couple walking into the sunset with the same book somewhere in the frame. Communicating the relevance of every life being significant to those that come after them...when a genealogy doesn't say enough about the details of ones life. Please note that I am open to the professionals own ideas...I am not locked into my concepts. On the back of the card I would like one or two phrases..."A Genealogy Doesn't Say Enough" and/or "Every life legacy is uniquely significant to the next generation".
Updates

I have added a couple of photos for ideas that may be used if needed.

I have both increased and committed the payment! Thanks for the reminder!

Reason: We increased the payment commitment and added some photo ideas to help.

We want to thank EVERYONE who participated in this contest. There were so many wonderful and VERY professional proposals...making it very challenging to decide on one! We are posting a new contest for a brochure now and hope many of you will participate. May God bless your endeavors.

Target Market(s)

Senior populous & baby boomer generation.

Industry/Entity Type

Business

Logo Text

Tales from Kin ordinary lives...extraordinary legacy

Requirements
Must have
• Relevant info:
Domain name: talesfromkin.com
email: info@talesfromkin.com
phone: 1-855-GAB-TALE toll free
1-717-382-5619 local
name: Doris Whitlock, M.A.
Nice to have
• photo of senior or senior couple....book with our web address on the binding. I attached two photos that could work if cropped and enhanced. Words need to be deleted from the one photo of senior at a writing desk and couple on the beach could use a sunset sky and other people cropped out. Just ideas...don't know if you have better ones or prefer a different idea.

```html
<!DOCTYPE html>
<html lang="en">
<head>
<meta charset="utf-8">
<title>Tales from Kin — Business Card</title>
<link rel="stylesheet" href="https://fonts.googleapis.com/css2?family=Monsieur+La+Doulaise&family=Overpass+Mono:wght@600&display=swap">
<style>
  :root {
    --sage: #c9d3bb;
    --sage-pale: #d3dbc6;
    --teal-wash: #a9c4bb;
    --sand: #d4c9a6;
    --sand-light: #dcd3b3;
    --ink: #1f231f;
    --rose-red: #e8264a;
    --white: #ffffff;
    --scene-dark: #2c3424;
    --scene-mid: #55603f;
    --scene-light: #b9c2a6;
    --scene-warm: #c9b994;
  }
  html, body {
    margin: 0;
    padding: 0;
    overflow: hidden;
    background: var(--sage);
  }
  .card {
    position: relative;
    width: 1200px;
    height: 702px;
    overflow: hidden;
    background: var(--sage);
  }
  .card__wash {
    position: absolute;
    inset: 0;
    width: 1200px;
    height: 702px;
  }
  .card__scene {
    position: absolute;
    left: 0;
    top: 0;
    width: 1200px;
    height: 702px;
  }
  .card__title {
    position: absolute;
    left: 140px;
    top: 110px;
    margin: 0;
    font-family: "Monsieur La Doulaise", cursive;
    font-weight: 400;
    font-size: 150px;
    line-height: 1;
    letter-spacing: 4px;
    color: var(--ink);
    white-space: nowrap;
  }
  .card__contact {
    position: absolute;
    left: 106px;
    top: 398px;
    font-family: "Overpass Mono", monospace;
    font-weight: 600;
  }
  .contact__name {
    margin: 0 0 16px;
    font-size: 28px;
    letter-spacing: 4px;
    color: var(--rose-red);
    text-transform: uppercase;
  }
  .contact__list {
    list-style: none;
    margin: 0;
    padding: 0;
    font-size: 26px;
    line-height: 39px;
    color: var(--ink);
  }
  .contact__note {
    color: var(--white);
    font-weight: 400;
  }
</style>
</head>
<body>
  <main class="card">
    <svg class="card__wash" viewBox="0 0 1200 702" aria-hidden="true">
      <path d="M0 0 H420 C400 20 360 30 330 18 C300 8 260 28 220 20 C160 10 120 30 60 24 C30 22 10 30 0 26 Z" fill="var(--teal-wash)" opacity="0.55"/>
      <path d="M640 0 H1200 V18 C1140 30 1080 10 1020 22 C960 32 900 12 840 20 C780 28 720 10 640 0 Z" fill="var(--teal-wash)" opacity="0.45"/>
      <path d="M0 610 C40 590 80 600 120 612 C170 628 210 598 260 604 C320 612 360 640 420 630 C480 620 520 600 560 612 L560 702 H0 Z" fill="var(--sand)"/>
      <path d="M0 540 C30 520 70 535 90 560 C110 590 60 610 0 600 Z" fill="var(--sage-pale)" opacity="0.8"/>
      <path d="M1040 640 C1090 620 1150 630 1200 640 V702 H1000 Z" fill="var(--sand)"/>
    </svg>

    <svg class="card__scene" viewBox="0 0 1200 702" role="img" aria-label="Photograph of an older couple walking away along a coastal path at dusk">
      <defs>
        <linearGradient id="sceneTone" x1="0" y1="0" x2="0" y2="1">
          <stop offset="0" stop-color="var(--scene-warm)"/>
          <stop offset="0.18" stop-color="var(--scene-light)"/>
          <stop offset="0.38" stop-color="var(--scene-mid)"/>
          <stop offset="0.7" stop-color="var(--scene-dark)"/>
          <stop offset="1" stop-color="var(--scene-mid)"/>
        </linearGradient>
      </defs>
      <path d="M700 262 L1110 262 L1180 300 L1150 330 L1190 360 L1130 380 L1180 420 L1110 440 L1160 480 L1080 505 L1140 540 L1070 560 L1110 600 L1040 640 L980 702 L700 702 L640 640 L560 560 L620 520 L540 490 L610 450 L560 420 L630 380 L590 350 L660 320 L620 290 Z" fill="url(#sceneTone)"/>
    </svg>

    <h1 class="card__title">Tales from Kin</h1>

    <section class="card__contact">
      <p class="contact__name">Doris Whitlock, M.A.,</p>
      <ul class="contact__list">
        <li>1-855-GAB-TALE <span class="contact__note">toll free</span></li>
        <li>1-717-382-5619 <span class="contact__note">local</span></li>
        <li>info@talesfromkin.com</li>
        <li>www.talesfromkin.com</li>
      </ul>
    </section>
  </main>
</body>
</html>
```